Boutique Salon Brand Refresh needs color palette, font, templates.

Toveli Hair Studio is an established hair salon celebrating 10 years in business. We are currently evolving our brand to better reflect who we are today, the clients we serve, and the direction we want to take our business moving forward.
Our goal is to position Toveli as a refined, modern boutique salon created specifically for “The Toveli Woman.”
In the past, much of our branding and marketing focused on us—our salon, our space, our services, and our team. Going forward, we want to shift that focus to her: who she is, what she values, how she wants to look and feel, and how Toveli fits into her life.
We want our brand to communicate expertise and quality without feeling overly luxurious, trendy, intimidating, or impersonal. It should feel polished, sophisticated, warm, approachable, and timeless—a boutique experience designed for women who value beautiful, healthy hair and trusted professional guidance.
As part of this rebrand, we are looking to establish a cohesive visual identity that can be carried consistently across our website, social media, email marketing, print materials, signage, and other client touchpoints.

*** For THIS PROJECT, we are SPECIFICALLY LOOKING for:
- A cohesive brand color palette
- 2–3 complementary fonts for consistent use across our marketing
- 4–5 customizable social media templates that can be used across Instagram and Facebook
A visual direction that feels distinctive to Toveli and speaks directly to The Toveli Woman.
The following information provides more detail about The Toveli Woman, our positioning, brand personality, values, and the overall direction we envision for the next chapter of Toveli Hair Studio.
Toveli Hair Studio
Mendham, NJ USA
tovelihairbrookvale.example

--PRIMARY AUDIENCE
The Toveli woman values quality, consistency, and professional guidance.
She wants to look polished and current without appearing overdone or overly trendy.
She may be managing grey hair, changing texture, thinning, dryness, fading color, or a style that no longer reflects who she is. She wants an expert who understands these concerns and can create a realistic plan.
She is willing to invest in professional services and products when she understands their value.
She does not want to experiment with her appearance.
She wants to feel confident in the person caring for her hair.
Women approximately 45 to 65 years old living in Mendham, Morris County, and surrounding communities.

--COLOR PALETTE
The overall appearance should feel calm, spacious, editorial, and cohesive. The entire visual system should feel more like a refined boutique hotel, skincare brand, or luxury lifestyle publication than a traditional salon advertisement.
When choosing the palette, we want the colors to invoke these feelings.
Represents:
Expertise
Confidence
Timelessness
Professionalism
Calm
Warmth
Cleanliness
Soft luxury
Natural beauty
Warmth
Balance
Subtle sophistication
Consistency

--TYPOGRAPHY
The typography system should feel refined, modern, readable, and timeless.
Recommended usage for each font, size, spacing, etc.

----TEMPLATE IDEAS
**EDUCATIONAL POST
Frequently asked questions
Healthy-hair advice
Healthy Hair Tip
Grey Coverage FAQ
Grey Blending FAQ
Product education
Single-tip graphic
**REVIEWS
Google reviews
Finest of Brookvale recognition/Community awards
Long-term guest relationships
Guest testimonials/satisfaction stories
Referral stories
**ADS
**SALON UPDATES/INFO
Holiday hours
Policy reminder
New guest guide
Consultation invitation
Service spotlight
Seasonal guidance
**ABOUT TOVELI
Who we are
What to expect from us
What we can provide
Our expertise
**HIGHLIGHT ICON
Questions
Testimonial
Product
Reminders

TEMPLATE RULES
Use the color palette
Use only the font system
Maintain generous spacing
Limit text
Use consistent margins
Keep calls to action simple
Avoid crowded layouts
Use photography intentionally
Keep every template recognizably Toveli

Target Market(s)

Women approximately 45 to 65 years old living in Mendham, Morris County, and surrounding communities. She values quality, consistency, and professional guidance. She wants to look polished and current without appearing overdone or overly trendy. She is willing to invest in professional services and products when she understands their value.

Industry/Entity Type

Hair Salon

Font styles to use
Serif
Sans Serif
Script

Requirements
Must have
• We are looking to establish a cohesive visual identity that can be carried consistently across platforms. It should communicate expertise and quality without feeling overly fluffy, trendy, intimidating, or impersonal. I would like to see multiple template ideas. Example- one template for education post, one template for reviews, one for salon information/updates. etc. My main goal here is to simplify social media posts by having designated templates for each post category. WE WILL BE KEEPING OUR ORGINAL LOGO- SO COLOR PALETTE MUST REFLECT THAT.
Nice to have
• Color palette and font sets that reflect the brand. **cohesive visual identity**
Should not have
• Nothing flashy, busy, overly trendy.

```html
<!DOCTYPE html>
<html lang="en">
<head>
<meta charset="utf-8">
<title>Toveli Hair Studio – Colour Offer</title>
<link rel="stylesheet" href="https://fonts.googleapis.com/css2?family=Gilda+Display&family=Playfair+Display:wght@400&family=Montserrat:wght@500&family=Josefin+Sans:wght@300&display=swap">
<style>
  :root {
    --paper: #ffffff;
    --linen: #e6e1dc;
    --espresso: #6f5441;
    --taupe: #a48a74;
    --rule: #8a7b6e;
    --logo: #8a7c70;
    --hair-dark: #2a1810;
    --hair-mid: #5a3522;
    --skin: #d9b8a0;
    --cream: #ece6df;
  }
  * { margin: 0; padding: 0; box-sizing: border-box; }
  html, body { width: 1200px; height: 1200px; overflow: hidden; background: var(--paper); }
  .post { position: relative; width: 1200px; height: 1200px; background: var(--paper); }

  .portrait {
    position: absolute; left: 0; top: 0; width: 399px; height: 1200px;
    background: linear-gradient(160deg, var(--cream) 0%, var(--hair-mid) 22%, var(--hair-dark) 45%, var(--skin) 62%, var(--hair-mid) 78%, var(--cream) 100%);
  }
  .linen-band { position: absolute; left: 399px; top: 0; width: 39px; height: 1200px; background: var(--linen); }

  .rule { position: absolute; left: 501px; width: 260px; height: 2px; background: var(--rule); }
  .rule--1 { top: 270px; } .rule--2 { top: 500px; } .rule--3 { top: 715px; } .rule--4 { top: 955px; }

  .offer {
    position: absolute; left: 500px; top: 86px;
    font-family: "Gilda Display", serif; font-size: 156px; line-height: 1;
    color: var(--espresso); letter-spacing: 1px; white-space: nowrap;
  }
  .urgency {
    position: absolute; left: 500px; top: 305px;
    font-family: "Gilda Display", serif; font-size: 80px; line-height: 95px;
    color: var(--taupe); text-transform: uppercase; letter-spacing: -1px;
  }
  .service {
    position: absolute; left: 500px; top: 527px;
    font-family: "Playfair Display", serif; font-size: 62px; line-height: 70px;
    color: var(--taupe);
  }
  .cta {
    position: absolute; left: 501px; top: 766px;
    font-family: "Montserrat", sans-serif; font-weight: 500; font-size: 57px; line-height: 74px;
    color: var(--taupe); letter-spacing: 8px; text-transform: uppercase; white-space: nowrap;
  }
  .brand { position: absolute; left: 500px; top: 990px; color: var(--logo); }
  .brand__name { font-family: "Gilda Display", serif; font-size: 118px; line-height: 1; }
  .brand__tag {
    margin-top: 22px; font-family: "Josefin Sans", sans-serif; font-weight: 300;
    font-size: 22px; letter-spacing: 10px; text-transform: uppercase;
  }
</style>
</head>
<body>
  <main class="post">
    <div class="portrait" role="img" aria-label="Photograph of a smiling woman with long wavy brunette hair, face half hidden at the edge"></div>
    <div class="linen-band"></div>

    <h1 class="offer">20% OFF</h1>
    <div class="rule rule--1"></div>
    <p class="urgency">Limited<br>Time Only</p>
    <div class="rule rule--2"></div>
    <p class="service">All Colour Services<br>this month</p>
    <div class="rule rule--3"></div>
    <p class="cta">Book Your<br>Appointment</p>
    <div class="rule rule--4"></div>

    <div class="brand">
      <div class="brand__name">Toveli</div>
      <div class="brand__tag">Hair Studio</div>
    </div>
  </main>
</body>
</html>
```